Kem7Dex Letterhead

Need a new letterhead for my law firm.
IDENTIFYING INFORMATION BELOW:
Ansel T Brightwater III
Attorney at Law
Address: 4832 Tillbury Rd, Ste 250, Dallas, TX 75204
Phone: 866-402-7183
Fax: 469-583-0271
Email: kem@kem7dex.example
Website: www.kem7dex.example

Colors
0054AA
0677BA
7BADD7
CADEEF
E8F1F8

Requirements
Must have
• Logo needs to be on the letterhead, along with identifying information which is included in the project description.

```html
<!DOCTYPE html>
<html lang="en">
<head>
<meta charset="utf-8">
<title>Kem7Dex Letterhead</title>
<link href="https://fonts.googleapis.com/css2?family=Source+Sans+3:wght@400;600;700&family=Arimo:wght@400&display=swap" rel="stylesheet">
<style>
  :root {
    --navy: #0054AA;
    --blue: #0677BA;
    --sky: #7BADD7;
    --mist: #CADEEF;
    --ink: #1d1d1f;
    --rule: #8a8f96;
    --backdrop: #e4e5e7;
    --paper: #fdfdfd;
  }
  * { margin: 0; padding: 0; box-sizing: border-box; }
  html, body {
    width: 1200px; height: 1013px; overflow: hidden;
    background: var(--backdrop);
  }
  .letterhead {
    position: absolute; left: 264px; top: 28px;
    width: 672px; height: 956px;
    background: var(--paper);
    font-family: "Source Sans 3", sans-serif;
    color: var(--ink);
  }
  .brand {
    position: absolute; left: 22px; top: 34px;
    display: flex; align-items: center; gap: 12px;
  }
  .brand-square { width: 22px; height: 22px; background: var(--blue); }
  .brand-name {
    font-size: 38px; font-weight: 700; line-height: 1;
    letter-spacing: 1px; color: var(--ink);
  }
  .attorney {
    position: absolute; left: 422px; top: 38px; width: 236px;
    color: var(--navy);
  }
  .attorney-name {
    font-size: 17.8px; font-weight: 700; letter-spacing: 0.5px;
    line-height: 1; white-space: nowrap;
  }
  .attorney-title {
    margin-top: 9px; padding-bottom: 5px; width: 154px;
    font-size: 11.5px; letter-spacing: 3.8px; line-height: 1;
    white-space: nowrap;
    border-bottom: 1px solid var(--rule);
  }
  .contact {
    margin-top: 9px;
    font-family: "Arimo", sans-serif; font-size: 9.8px; line-height: 12px;
    border-collapse: collapse;
  }
  .contact th { font-weight: 400; text-align: left; vertical-align: top; width: 49px; }
  .contact td, .contact th { padding-bottom: 5.3px; }
  .body-copy {
    position: absolute; left: 40px; top: 255px; width: 596px;
    font-size: 13px; line-height: 16.5px; text-align: justify;
  }
  .body-copy p + p { margin-top: 41px; }
  .signature {
    position: absolute; left: 48px; top: 724px;
    width: 90px; height: 52px;
    background: linear-gradient(100deg, rgba(29,29,31,0.08), rgba(29,29,31,0.03));
    border-radius: 26px;
  }
  .footer-band {
    position: absolute; left: 0; bottom: 11px; width: 672px; height: 9px;
    background: linear-gradient(90deg, var(--navy), var(--blue) 60%, var(--navy));
  }
</style>
</head>
<body>
  <main class="letterhead">
    <header>
      <div class="brand">
        <span class="brand-square"></span>
        <span class="brand-name">Kem7Dex</span>
      </div>
      <div class="attorney">
        <h1 class="attorney-name">ANSEL T BRIGHTWATER III</h1>
        <p class="attorney-title">ATTORNEY AT LAW</p>
        <table class="contact">
          <tr><th>Phone:</th><td>866-402-7183</td></tr>
          <tr><th>Fax:</th><td>469-583-0271</td></tr>
          <tr><th>Email:</th><td>kem@kem7dex.example</td></tr>
          <tr><th>Website:</th><td>www.kem7dex.example</td></tr>
          <tr><th>Address:</th><td>4832 Tillbury Rd, Ste 250,<br>Dallas, TX 75204</td></tr>
        </table>
      </div>
    </header>

    <section class="body-copy">
      <p>Lorem ipsum dolor sit amet, consectetur adipisicing elit, sed do eiusmod tempor incididunt ut labore et dolore magna aliqua. Ut enim ad minim veniam, quis nostrud exercitation ullamco laboris nisi ut aliquip ex ea commodo consequat. Duis aute irure dolor in reprehenderit in voluptate velit esse cillum dolore eu fugiat nulla pariatur. Excepteur sint occaecat cupidatat non proident, sunt in culpa qui officia deserunt mollit anim id est laborum. Sed ut perspiciatis unde omnis iste natus error sit voluptatem accusantium doloremque laudantium, totam rem aperiam, eaque ipsa quae ab illo inventore veritatis et quasi architecto beatae vitae dicta sunt explicabo. Nemo enim ipsam voluptatem quia voluptas sit aspernatur aut odit aut fugit, sed quia consequuntur magni dolores eos qui ratione voluptatem sequi nesciunt. Neque porro voluptatem sequi nesciunt. Nemo enim ipsam voluptatem quia voluptas.</p>
      <p>Lorem ipsum dolor sit amet, consectetur adipisicing elit, sed do eiusmod tempor incididunt ut labore et dolore magna aliqua. Ut enim ad minim veniam, quis nostrud exercitation ullamco laboris nisi ut aliquip ex ea commodo consequat. Duis aute irure dolor in reprehenderit in voluptate velit esse cillum dolore eu fugiat nulla pariatur. Excepteur sint occaecat cupidatat non proident, sunt in culpa qui officia deserunt mollit anim id est laborum. Sed ut perspiciatis unde omnis iste natus error sit voluptatem accusantium doloremque laudantium, totam rem aperiam, eaque ipsa quae ab illo inventore veritatis et quasi architecto beatae vitae dicta sunt explicabo. Nemo enim ipsam voluptatem quia voluptas sit aspernatur aut odit aut.</p>
      <p>Lorem ipsum dolor sit amet, consectetur adipisicing elit, sed do eiusmod tempor incididunt ut labore et dolore magna aliqua. Ut enim ad minim veniam, quis nostrud exercitation ullamco laboris nisi ut aliquip ex ea commodo consequat. .</p>
    </section>

    <div class="signature" role="img" aria-label="Handwritten signature"></div>

    <div class="footer-band" aria-hidden="true"></div>
  </main>
</body>
</html>
```